Webdesign Chiropraktik
Zielgruppe
Amerikanische Chiropraktik
Aufgabenstellung
keine direkten vorgaben...Wir sind ein junges Team und brauchen eine moderne ansprechende Webseite...

```html
<!DOCTYPE html>
<html lang="de">
<head>
<meta charset="utf-8">
<title>Chiropraktik in Aldenhofen</title>
<link rel="stylesheet" href="https://fonts.googleapis.com/css2?family=Lato:wght@300;400;700&display=swap">
<style>
:root{
  --green:#9dbf2c;
  --green-dark:#4a9a22;
  --yellow:#f5e33a;
  --ink:#1f1f1f;
  --muted:#7a7a7a;
  --cream:#fbfdf1;
  --white:#ffffff;
}
*{box-sizing:border-box;margin:0;padding:0}
html,body{width:1200px;height:4290px;overflow:hidden}
body{position:relative;font-family:'Lato',sans-serif;color:var(--ink);background:var(--white)}
.abs{position:absolute}
.hero{left:0;top:0;width:1200px;height:521px;background:linear-gradient(135deg,#3a2f29 0%,#b58a73 40%,#e8cbb8 60%,#2e2a28 100%)}
.hero-card{left:258px;top:100px;width:604px;height:354px;background:rgba(255,255,255,.82)}
.brand-mark{position:absolute;left:40px;top:60px;width:180px;text-align:center;color:var(--green);font-size:20px;font-weight:700;line-height:1.3}
.brand-mark .dot{display:block;width:64px;height:64px;border-radius:50%;background:var(--green);margin:0 auto 14px;opacity:.85}
.info{font-size:13px;line-height:20px;color:var(--ink)}
.info h3{font-weight:400;color:var(--green);font-size:16px;margin-bottom:16px}
.info .lead{margin-bottom:22px}
.info .row{display:flex;gap:10px;align-items:flex-start}
.info svg{width:14px;height:14px;margin-top:3px;flex:none}
.info .addr{margin-bottom:18px}
.info table{border-collapse:collapse;margin-top:18px;font-size:13px}
.info td{padding:0;line-height:20px}
.info td:first-child{width:80px}
.nav{left:0;top:521px;width:1200px;height:58px;background:linear-gradient(90deg,var(--green-dark),#9cc62e 55%,var(--yellow));display:flex;align-items:center;padding-left:203px;gap:23px}
.nav a{color:var(--white);font-weight:700;font-size:16px;text-decoration:none;letter-spacing:.3px}
.nav .call{background:var(--white);color:var(--green);padding:10px 17px;margin-left:0;border-radius:2px}
.title-green{color:var(--green);font-weight:400;font-size:34px;text-align:center;width:1200px;left:0}
.section-title{font-weight:400;font-size:34px;text-align:center;width:1200px;left:0;color:var(--ink)}
.photo{background:linear-gradient(135deg,#cfc3ae,#8a7a64 50%,#3b3a37)}
.intro-text{left:567px;top:714px;width:520px;font-size:14px;line-height:18px;color:#333}
.intro-text p{margin-bottom:18px}
.btn{display:inline-block;background:var(--green);color:var(--white);font-weight:700;font-size:15px;text-decoration:underline;text-align:center;line-height:42px;height:42px;box-shadow:0 3px 6px rgba(0,0,0,.25)}
.band{left:0;width:1200px;background:var(--cream)}
.card{width:313px;height:477px;background:var(--white);box-shadow:0 2px 6px rgba(0,0,0,.18)}
.card .pic{height:190px;background:linear-gradient(135deg,#e9e4da,#8c8378 55%,#2b2b2b)}
.card h4{color:var(--green);font-weight:400;font-size:19px;margin:30px 42px 12px}
.card p{color:var(--muted);font-size:12.5px;line-height:16px;margin:0 42px 16px;font-weight:300}
.bio{background:var(--cream)}
.bio h5{font-weight:400;font-size:16px}
.bio .role{color:var(--green);font-size:16px;margin-bottom:18px}
.cv{font-size:12px;line-height:20px;color:#333;border-collapse:collapse}
.cv td{padding:0 12px 0 0;vertical-align:top}
.bio ul{list-style:none;font-size:12px;line-height:20px;color:#333}
.bio ul li::before{content:"•";margin-right:8px}
.bio .small li{font-size:11px;line-height:20px}
.termine{left:496px;top:3512px;font-size:13px;line-height:20px}
.map{background:linear-gradient(135deg,#eeeeee 0%,#f4f4f4 55%,#cfe8c9 70%,#a9d3e6 80%,#cfe8c9 90%);border:1px solid #888}
</style>
</head>
<body>

<header class="hero abs" role="img" aria-label="Foto: Hände eines Chiropraktikers bei der Behandlung am Rücken"></header>
<div class="hero-card abs">
  <div class="brand-mark"><span class="dot"></span>Chiropraktik Aldenhofen</div>
  <div class="info abs" style="left:296px;top:28px">
    <h3>Chiropraktik in Aldenhofen</h3>
    <p class="lead">Wir freuen uns auf Ihren Besuch!</p>
    <div class="row addr"><svg viewBox="0 0 24 24"><path d="M12 2a7 7 0 0 0-7 7c0 5 7 13 7 13s7-8 7-13a7 7 0 0 0-7-7zm0 9.5A2.5 2.5 0 1 1 12 6.5a2.5 2.5 0 0 1 0 5z" fill="#1f1f1f"/></svg><span>Lindenhofweg 14<br>85990 Aldenhofen</span></div>
    <div class="row"><svg viewBox="0 0 24 24"><path d="M6.6 10.8a15 15 0 0 0 6.6 6.6l2.2-2.2a1 1 0 0 1 1-.25 11 11 0 0 0 3.6.6 1 1 0 0 1 1 1V20a1 1 0 0 1-1 1A17 17 0 0 1 3 4a1 1 0 0 1 1-1h3.5a1 1 0 0 1 1 1 11 11 0 0 0 .6 3.6 1 1 0 0 1-.25 1z" fill="#1f1f1f"/></svg><span>08199 4471250</span></div>
    <div class="row"><svg viewBox="0 0 24 24"><path d="M3 9l9-6 9 6v11H3z" fill="#1f1f1f"/></svg><span>info@chiropraktik-aldenhofen.de</span></div>
    <table><tr><td>Montag</td><td>13:00-20:00 Uhr</td></tr><tr><td>Dienstag</td><td>10:00-17:00 Uhr</td></tr><tr><td>Mittwoch</td><td>13:00-20:00 Uhr</td></tr><tr><td>Donnerstag</td><td>08:00-15:00 Uhr</td></tr><tr><td>Freitag</td><td>&nbsp;&nbsp;&nbsp;&nbsp;&nbsp;&nbsp;&nbsp;&nbsp;geschlossen</td></tr></table>
  </div>
</div>

<nav class="nav abs">
  <a href="#">HOME</a><a href="#">ABLAUF</a><a href="#">ÜBER UNS</a><a href="#">ANFAHRT</a><a href="#">AMNESEBOGEN</a>
  <a href="#" class="call">JETZT ANRUFEN: 08199 447 1250</a>
</nav>

<h1 class="title-green abs" style="top:622px">Chiropraktik in Aldenhofen</h1>
<div class="photo abs" style="left:0;top:696px;width:518px;height:394px" role="img" aria-label="Foto: Behandlungsraum mit Liegen und Wandbild"></div>
<div class="intro-text abs">
  <p>Die Chiropraktik beschäftigt sich primär mit den Störungen des Nervensystems im Körper.</p>
  <p>Gibt es in unserem Hauptorgan (Gehirn) einen Fehler/Schwäche kann sich das in unserem Körper spiegeln! Meistens reagiert der Körper mit einer lokalen Verspannung eines Muskels. Daraus kann eine Einschränkung der Gelenkbeweglichkeit resultieren. Der Chiropraktiker muss also mittels neurologischen Tests herausfinden, wo sich der Fehler im Gehirn befindet.</p>
  <p>Durch gezielte Justierungen an der Wirbelsäule und an peripheren Gelenken kann der Chiropraktiker das Gehirn positiv beeinflussen. Je weniger Fehler im Gehirn, desto besser die Funktion des Körpers -&gt; WENIGER Symptome!</p>
  <p>Wird das Gehirn, wie bei allen Aktivitäten, regelmäßig positiv stimuliert, gibt es sowohl im Gehirn als auch im Körper positive Veränderungen. Heilung ist also ein Prozess und kein Event.</p>
</div>
<a class="btn abs" style="left:567px;top:1033px;width:235px">Jetzt Termin vereinbaren</a>

<section class="band abs" style="top:1137px;height:752px"></section>
<h2 class="section-title abs" style="top:1182px">Der Ablauf</h2>
<div class="card abs" style="left:85px;top:1283px">
  <div class="pic" role="img" aria-label="Foto: Anamnesegespräch"></div>
  <h4>Amnesegespräch</h4>
  <p>Der Ersttermin umfasst ein ausführliches Anamnesegespräch, eine körperliche Untersuchung und die anschließende Behandlung (Justierung). Nach dieser Sitzung wird ein individueller Behandlungsplan für Sie erstellt.</p>
  <p>In dem Anamnesegespräch erzählen Sie uns ausführlich IHR Hauptproblem. Die mögliche Ursache wird detailliert besprochen.</p>
</div>
<div class="card abs" style="left:443px;top:1283px">
  <div class="pic" role="img" aria-label="Foto: Untersuchung auf der Liege"></div>
  <h4>Untersuchung</h4>
  <p>In der körperlichen Untersuchung wird der ganze Körper in Statik und aktiver Beweglichkeit getestet.</p>
  <p>Nachdem Ihnen, anhand eines Bildes, Ihre Körperhaltung gezeigt wurde, erfolgen mehrere neurologische Testungen, um die Fehler des Nervensystems herauszufinden.</p>
</div>
<div class="card abs" style="left:805px;top:1283px">
  <div class="pic" role="img" aria-label="Foto: Justierung an der Wirbelsäule"></div>
  <h4>Fehleranalyse und Ziel</h4>
  <p>Ist der Fehler klar, wird der Körper justiert. Mittels sanfter Impulse an der Wirbelsäule und peripheren Gelenken wird das Nervensystem positiv angeregt.</p>
  <p>Das Ziel ist den Fehler zu beheben. Folglich schwinden Ihre Symptome automatisch.</p>
</div>
<a class="btn abs" style="left:486px;top:1804px;width:236px">Jetzt Termin vereinbaren</a>

<h2 class="section-title abs" style="top:1935px">Über Uns</h2>
<div class="photo abs" style="left:98px;top:2035px;width:311px;height:403px" role="img" aria-label="Foto: Chiropraktiker mit Wirbelsäulenmodell"></div>
<div class="bio abs" style="left:454px;top:2035px;width:678px;height:403px;padding:20px 24px">
  <h5>Jonas Weidacher</h5>
  <p class="role">Chiropraktiker, Heilpraktiker und Physiotherapeut</p>
  <table class="cv">
    <tr><td>2020 - 2023</td><td>Student an der Hochschule Talberg für "Master of Science in Chiropractic"</td></tr>
    <tr><td>2017 - 2019</td><td>Ausbildung zum Chiropraktiker am Chiropraktik Forum Nordstadt</td></tr>
    <tr><td>2014 - 2018</td><td>sämtliche Fortbildungen und Seminare mit dem Schwerpunkt Chiropraktik</td></tr>
    <tr><td>2016 - 2017</td><td>Zertifizierter Therapeut für Chiropraktik beim Institut für Manuelle Medizin Westend</td></tr>
    <tr><td>2015 - 2017</td><td>Nebenberufliche Ausbildung zum Heilpraktiker</td></tr>
    <tr><td>2011 - 2014</td><td>Ausbildung zum Physiotherapeuten in Rosenau</td></tr>
  </table>
  <p style="font-size:12px;font-weight:700;margin:20px 0 2px">weitere Kenntnisse:</p>
  <ul><li>Manuelle Lymphdrainage</li><li>Manuelle Therapie nach Maitland</li><li>Neutraltherapie</li><li>Plasmatherapie (PRP)</li><li>Labordiagnostik/ Injektions- und Infusionskurse</li></ul>
</div>

<div class="bio abs" style="left:98px;top:2484px;width:672px;height:403px;padding:20px 23px">
  <h5>Lukas Brenner</h5>
  <p class="role">Heilpraktiker/Chiropraktiker</p>
  <ul class="small">
    <li>3-jähriges Vollzeit-Studium zum Heilpraktiker an der renommierten Lorenz-Haller-Schule in Rosenau (Berufsfachschule)</li>
    <li>4-monatige Ausbildung am Lehrinstitut Aurelia Rosenau</li>
    <li>4-monatige Ausbildung am ZNM Rosenau (Zentrum für Naturheilkunde)</li>
    <li>2016 Erlaubnis zur Ausübung der Heilkunde beim Gesundheitsamt Rosenau (staatliche Heilpraktikerprüfung)</li>
    <li>Seit 2017 eigene Praxis in Oberfelden bei Rosenau</li>
    <li>Assistenz bei Georg Feldmair (Heilpraktiker, Sportphysiotherapeut, Osteopathie)</li>
    <li>Ausbildungsreihe Brain-Based Chiropraktik Akademie sowie Mastery Modul bei Martin Kessler am Spinalforum<br>&nbsp;&nbsp;&nbsp;Nordstadt (Neurobasierte Chiropraktik)</li>
    <li>Doppelte Teilnahme an der Full Spine Chiropraktik Seminarreihe bei Jonas Weidacher und Daniel Rauch (SpineCrew)</li>
    <li>6 Monate Hospitation bei Chiropraxis Weidacher</li>
    <li>zusätzlich spezifische Fortbildungen in den angebotenen Verfahren (u.a. Chirotage Waldbrunn)</li>
    <li>Mitglied im Heilpraktikerbund Süd e.V.</li>
  </ul>
</div>
<div class="photo abs" style="left:819px;top:2484px;width:313px;height:403px;background:linear-gradient(135deg,#d9c7b4,#a38a73 50%,#3bbfa6)" role="img" aria-label="Foto: Heilpraktiker im türkisen Shirt"></div>

<div class="bio abs" style="left:454px;top:2937px;width:678px;height:399px;padding:25px 24px">
  <h5>Annika</h5>
  <p class="role">Chiropraktische Assistenz</p>
  <p style="font-size:15px;line-height:20px;color:#333;margin-bottom:20px">Ist für unser Praxismanagement verantwortlich.</p>
  <p style="font-size:15px;line-height:20px;color:#333">Haben Sie Fragen oder Anregungen?<br>Dann ist Annika die richtige Ansprechperson für Sie!</p>
</div>
<a class="btn abs" style="left:479px;top:3133px;width:235px">Jetzt Termin vereinbaren</a>

<section class="band abs" style="top:3433px;height:336px"></section>
<h2 class="section-title abs" style="top:3458px">Termine</h2>
<div class="termine abs info">
  <p style="margin-bottom:18px">Wir freuen uns auf Ihren Besuch!</p>
  <table style="margin-top:0"><tr><td style="width:98px">Montag</td><td>13:00-20:00 Uhr</td></tr><tr><td>Dienstag</td><td>10:00-17:00 Uhr</td></tr><tr><td>Mittwoch</td><td>13:00-20:00 Uhr</td></tr><tr><td>Donnerstag</td><td>08:00-15:00 Uhr</td></tr><tr><td>Freitag</td><td>&nbsp;&nbsp;&nbsp;&nbsp;&nbsp;&nbsp;&nbsp;&nbsp;&nbsp;&nbsp;&nbsp;geschlossen</td></tr></table>
</div>
<a class="btn abs" style="left:483px;top:3687px;width:235px">Jetzt Termin vereinbaren</a>

<h2 class="section-title abs" style="top:3793px">Anfahrt</h2>
<div class="brand-mark abs" style="left:150px;top:3960px;width:190px">
  <span class="dot"></span>Chiropraktik Aldenhofen
</div>
<div class="map abs" style="left:424px;top:3882px;width:335px;height:323px" role="img" aria-label="Karte: Lage der Praxis am Fluss"></div>
<div class="info abs" style="left:835px;top:3880px">
  <h3>Chiropraktik in Aldenhofen</h3>
  <p class="lead">Wir freuen uns auf Ihren Besuch!</p>
  <div class="row addr"><svg viewBox="0 0 24 24"><path d="M12 2a7 7 0 0 0-7 7c0 5 7 13 7 13s7-8 7-13a7 7 0 0 0-7-7zm0 9.5A2.5 2.5 0 1 1 12 6.5a2.5 2.5 0 0 1 0 5z" fill="#1f1f1f"/></svg><span>Lindenhofweg 14<br>85990 Aldenhofen</span></div>
  <div class="row"><svg viewBox="0 0 24 24"><path d="M6.6 10.8a15 15 0 0 0 6.6 6.6l2.2-2.2a1 1 0 0 1 1-.25 11 11 0 0 0 3.6.6 1 1 0 0 1 1 1V20a1 1 0 0 1-1 1A17 17 0 0 1 3 4a1 1 0 0 1 1-1h3.5a1 1 0 0 1 1 1 11 11 0 0 0 .6 3.6 1 1 0 0 1-.25 1z" fill="#1f1f1f"/></svg><span>08199 4471250</span></div>
  <div class="row"><svg viewBox="0 0 24 24"><path d="M3 9l9-6 9 6v11H3z" fill="#1f1f1f"/></svg><span>info@chiropraktik-aldenhofen.de</span></div>
  <table><tr><td>Montag</td><td>13:00-20:00 Uhr</td></tr><tr><td>Dienstag</td><td>10:00-17:00 Uhr</td></tr><tr><td>Mittwoch</td><td>13:00-20:00 Uhr</td></tr><tr><td>Donnerstag</td><td>08:00-15:00 Uhr</td></tr><tr><td>Freitag</td><td>&nbsp;&nbsp;&nbsp;&nbsp;&nbsp;&nbsp;&nbsp;&nbsp;geschlossen</td></tr></table>
</div>

</body>
</html>
```